The 50 Year History of the Moorfield Harrier Coursing Society

The Moorfield Harrier Coursing Society has been established for 50 years last month. We are putting together a chronological history book with interesting stories about events over the past 50 years.
Book title: Swift Across Ages: 50 Years of the Moorfield Harrier Coursing Society
Front Cover: We are looking for a simple but striking design. It must have at least one racing greyhound (image from Australia). I can supply images of greyhounds if required. It must have our logo.
Back Cover: can be minimal with club details
Book Size: A4

```html
<!DOCTYPE html>
<html lang="en">
<head>
<meta charset="utf-8">
<title>The 50 Year History of the Moorfield Harrier Coursing Society – Cover Spread</title>
<link rel="stylesheet" href="https://fonts.googleapis.com/css2?family=Bebas+Neue&family=Playfair+Display:ital,wght@1,500&family=Carlito&display=swap">
<style>
  :root {
    --backdrop: #262626;
    --green-deep: #0b5a0c;
    --green-mid: #138a14;
    --green-bright: #1c9e1c;
    --green-shadow: #093a0a;
    --gold: #e2ae2a;
    --gold-light: #f6d060;
    --gold-dark: #b9841a;
    --white: #ffffff;
    --brand-green: #1f8c1f;
  }
  * { margin: 0; padding: 0; box-sizing: border-box; }
  html, body { width: 1200px; height: 1200px; overflow: hidden; background: var(--backdrop); }

  .spread {
    position: absolute;
    left: 50px; top: 232px;
    width: 1100px; height: 735px;
    display: flex;
  }
  .cover, .spine {
    position: relative;
    height: 100%;
    overflow: hidden;
    background: radial-gradient(ellipse at 50% 8%, var(--green-bright) 0%, var(--green-mid) 35%, var(--green-deep) 100%);
  }
  .cover { width: 515px; }
  .spine { width: 70px; background: linear-gradient(90deg, var(--green-deep), var(--green-mid) 50%, var(--green-deep)); }

  .race-photo {
    position: absolute;
    left: 0; right: 0; top: 56%; height: 32.5%;
    background:
      radial-gradient(ellipse 45% 40% at 62% 45%, rgba(60,170,60,0.55) 0%, rgba(60,170,60,0) 100%),
      radial-gradient(ellipse 30% 35% at 28% 40%, rgba(5,40,5,0.7) 0%, rgba(5,40,5,0) 100%),
      linear-gradient(180deg, #0f6a10 0%, var(--green-shadow) 30%, #125a12 75%, #0c460c 100%);
  }
  .back .race-photo { top: 52%; height: 36.5%; opacity: 0.85; }
  .white-band {
    position: absolute;
    left: 0; right: 0; bottom: 0; height: 11.5%;
    background: var(--white);
    display: flex; align-items: center;
  }
  .club-name {
    font-family: "Bebas Neue", sans-serif;
    font-size: 24px;
    letter-spacing: 1px;
    color: var(--brand-green);
  }

  /* Title block */
  .title-block { position: absolute; left: 38px; right: 38px; }
  .rule { height: 3px; background: linear-gradient(90deg, var(--gold-dark), var(--gold-light), var(--gold)); }
  .kicker {
    display: flex; align-items: center; justify-content: space-between;
    white-space: nowrap;
    font-family: "Bebas Neue", sans-serif; color: var(--white); line-height: 1;
  }
  .fifty {
    font-family: "Playfair Display", serif; font-style: italic; font-weight: 500;
    color: var(--gold); line-height: 1;
  }
  .name-line {
    font-family: "Bebas Neue", sans-serif; color: var(--white);
    line-height: 0.9; text-align: center; white-space: nowrap;
  }
  .sub-line {
    display: flex; align-items: center; gap: 12px;
    font-family: "Bebas Neue", sans-serif; color: var(--gold); white-space: nowrap;
  }
  .sub-line .rule { flex: 1; }

  /* Front */
  .front .title-block { top: 60px; }
  .front .kicker { font-size: 48px; margin: 2px 0; }
  .front .fifty { font-size: 92px; margin-top: -14px; }
  .front .name-line.medium { font-size: 84px; margin-top: 12px; }
  .front .name-line.large { font-size: 156px; }
  .front .sub-line { font-size: 30px; letter-spacing: 5px; margin-top: 10px; }
  .front .white-band { justify-content: center; }
  .front .club-name { font-size: 26px; }

  /* Back */
  .back .title-block { top: 66px; }
  .back .kicker { font-size: 40px; margin: 0; }
  .back .fifty { font-size: 76px; margin-top: -10px; }
  .back .name-line.small { font-size: 29px; margin-top: 10px; text-align: left; }
  .blurbs {
    position: absolute; left: 38px; right: 38px; top: 215px;
    display: flex; flex-direction: column; gap: 26px;
  }
  .blurb {
    font-family: "Carlito", sans-serif; font-size: 13px; line-height: 1.4;
    color: var(--white); text-align: justify;
  }
  .back .white-band { padding-left: 38px; }

  /* Spine */
  .spine-title {
    position: absolute; left: 0; right: 0; top: 34px;
    display: flex; justify-content: center; align-items: center;
    writing-mode: vertical-rl;
    font-family: "Bebas Neue", sans-serif; font-size: 20px; letter-spacing: 2px;
    color: var(--white); white-space: nowrap;
  }
  .spine-title .fifty { font-size: 28px; margin: 6px 0; }
  .spine .white-band { justify-content: center; }
  .spine .club-name { font-size: 10px; letter-spacing: 0; text-align: center; line-height: 1; }
</style>
</head>
<body>
  <main class="spread">
    <section class="cover back">
      <div class="race-photo" role="img" aria-label="Racing hounds in coloured jackets sprinting along the track, tinted green"></div>
      <header class="title-block">
        <div class="rule"></div>
        <div class="kicker"><span>The</span><span class="fifty">50</span><span>Year History of</span></div>
        <div class="rule"></div>
        <div class="name-line small">The Moorfield Harrier Coursing Society</div>
      </header>
      <div class="blurbs">
        <p class="blurb">Lorem ipsum dolor sit amet, consectetur adipiscing elit, sed do eiusmod tempor incididunt ut labore et dolore magna aliqua. Quis ipsum suspendisse ultrices gravida. Risus commodo viverra maecenas accumsan lacus vel facilisis. Lorem ipsum dolor sit amet, consectetur adipiscing elit, sed do eiusmod tempor incididunt ut labore et dolore magna aliqua. Quis ipsum suspendisse ultrices gravida. Risus commodo viverra maecenas accumsan lacus vel facilisis. Lorem ipsum dolor sit amet, consectetur adipiscing elit, sed do eiusmod tempor incididunt ut labore et dolore magna aliqua. Quis ipsum suspendisse ultrices gravida. Risus commodo viverra maecenas accumsan lacus vel facilisis.</p>
        <p class="blurb">Lorem ipsum dolor sit amet, consectetur adipiscing elit, sed do eiusmod tempor incididunt ut labore et dolore magna aliqua. Quis ipsum suspendisse ultrices gravida. Risus commodo viverra maecenas accumsan lacus vel facilisis. Lorem ipsum dolor sit amet, consectetur adipiscing elit, sed do eiusmod tempor incididunt ut labore et dolore magna aliqua. Quis ipsum suspendisse ultrices gravida. lacus vel facilisis. Lorem ipsum dolor sit amet, consectetur adipiscing elit, sed do eiusmod tempor incididunt ut labore et dolore magna aliqua. Quis ipsum suspendisse ultrices gravida. Risus commodo viverra maecenas accumsan lacus vel facilisis. Lorem ipsum dolor sit amet, consectetur adipiscing elit, sed do eiusmod tempor incididunt ut labore et dolore magna aliqua. Quis ipsum suspendisse ultrices gravida. lacus vel facilisis.</p>
      </div>
      <footer class="white-band"><span class="club-name">Moorfield Harrier Coursing Society</span></footer>
    </section>

    <section class="spine">
      <div class="spine-title"><span>The</span><span class="fifty">50</span><span>Year History of the Moorfield Harrier Coursing Society</span></div>
      <footer class="white-band"><span class="club-name">Moorfield<br>Harrier</span></footer>
    </section>

    <section class="cover front">
      <div class="race-photo" role="img" aria-label="Racing greyhounds in numbered jackets at full stretch on the track, tinted green"></div>
      <header class="title-block">
        <div class="rule"></div>
        <div class="kicker"><span>The</span><span class="fifty">50</span><span>Year History of</span></div>
        <div class="rule"></div>
        <div class="name-line medium">The Moorfield</div>
        <div class="name-line large">Harrier</div>
        <div class="sub-line"><span class="rule"></span><span>Coursing Society</span><span class="rule"></span></div>
      </header>
      <footer class="white-band"><span class="club-name">Moorfield Harrier Coursing Society</span></footer>
    </section>
  </main>
</body>
</html>
```